Velmar Industrial Coatings

We are looking to improve our business cards. Our company installs industrial floor and wall coatings in industrial, chemical and food processing plants.
Our coatings which consist of epoxy, urethane, and vinyl esters provide chemical and abrasion resistant surface with non-skid properties that are easy to clean.

Target Market(s)

food manufacturing, chemical plants, breweries and wineries, warehouses, clean room floors.

Industry/Entity Type

Construction

Contact Information for Business Card

improved current logo.

Colors

Designer to choose colors to be used in the design.

Requirements
Must have
• the information from uploaded file
Nice to have
• "We'll be outstanding on your floors."

```html
<!DOCTYPE html>
<html lang="en">
<head>
<meta charset="utf-8">
<title>Velmar Industrial Coatings – Business Card</title>
<link rel="stylesheet" href="https://fonts.googleapis.com/css2?family=Montserrat:wght@400;500&display=swap">
<style>
  :root {
    --stage: #9a9a9a;
    --card-dark: #3d3d3d;
    --card-light: #ffffff;
    --brand-red: #d0161f;
    --ink: #3a3a3a;
    --ink-soft: #555555;
  }
  * { box-sizing: border-box; margin: 0; padding: 0; }
  html, body { width: 1200px; height: 930px; overflow: hidden; }
  body {
    background: var(--stage);
    display: flex;
    flex-direction: column;
    align-items: center;
    justify-content: center;
    gap: 40px;
    font-family: "Montserrat", sans-serif;
  }
  .card {
    width: 700px;
    height: 400px;
    border-radius: 28px;
    position: relative;
    box-shadow: 0 6px 18px rgba(0,0,0,0.25);
  }
  .card--front { background: var(--card-dark); display: flex; align-items: center; justify-content: center; }
  .card--back { background: var(--card-light); }

  .company-name {
    font-family: "Montserrat", sans-serif;
    font-weight: 500;
    color: var(--brand-red);
    text-transform: uppercase;
    letter-spacing: 1px;
    line-height: 1.25;
    text-align: center;
  }
  .card--front .company-name { font-size: 34px; }

  .card--back .company-name {
    position: absolute;
    left: 40px;
    top: 225px;
    width: 280px;
    font-size: 21px;
  }

  .divider {
    position: absolute;
    left: 345px;
    top: 95px;
    width: 2px;
    height: 215px;
    background: var(--brand-red);
  }
  .contact {
    position: absolute;
    left: 375px;
    top: 75px;
    color: var(--ink);
  }
  .contact__name { font-size: 27px; font-weight: 500; color: var(--brand-red); letter-spacing: 1px; text-transform: uppercase; }
  .contact__title { font-size: 15px; color: var(--ink-soft); margin: 2px 0 18px 22px; }
  .contact__address { font-size: 15px; line-height: 1.35; margin: 0 0 14px 22px; }
  .contact__list { list-style: none; font-size: 15px; line-height: 1.6; margin-left: 22px; }
  .contact__list li { display: flex; align-items: center; gap: 9px; }
  .contact__list svg { width: 12px; height: 12px; fill: none; stroke: var(--brand-red); stroke-width: 2; }
</style>
</head>
<body>
  <section class="card card--front" aria-label="Card front">
    <p class="company-name">Velmar Industrial<br>Coatings Inc.</p>
  </section>

  <section class="card card--back" aria-label="Card back">
    <p class="company-name">Velmar Industrial<br>Coatings Inc.</p>
    <div class="divider"></div>
    <div class="contact">
      <p class="contact__name">Daniel Harrow</p>
      <p class="contact__title">Director</p>
      <p class="contact__address">2580 Ne Alder St.<br>Riverton, Oregon 97388</p>
      <ul class="contact__list">
        <li><svg viewBox="0 0 12 12"><path d="M2 1.5 L4.5 1.5 L5.5 4 L4 5 Q5 7.5 7 8 L8 6.5 L10.5 7.5 L10.5 10 Q5 10.5 2 1.5Z" fill="#d0161f" stroke="none"/></svg>(555) 318-4206</li>
        <li><svg viewBox="0 0 12 12"><rect x="1" y="2.5" width="10" height="7"/><path d="M1 2.5 L6 6.5 L11 2.5"/></svg>info@velmarindustrial.com</li>
        <li><svg viewBox="0 0 12 12"><circle cx="6" cy="6" r="4.8"/><path d="M1.2 6 H10.8 M6 1.2 Q3 6 6 10.8 M6 1.2 Q9 6 6 10.8"/></svg>www.velmarindustrial.com</li>
      </ul>
    </div>
  </section>
</body>
</html>
```